Trip-Hop Instrumental Album from Producer Dario Welk needs a Front/Back Cover Design!

I need a CD cover design for the front and back of an instrumental hip-hop album that I've composed (so that I could print CD's or vinyls if I want to). The title of the album is Marrow Tide, and the artist name is Dario Welk. I'd like just the name of the album and the artist name on the front, and then the tracklisting on the back. The album is a collection of trippy hip-hop instrumentals, and the tracklisting is as follows:

Quiet on Halden
Glass Ember
Rust and Hollow
Slow Hymn for the Harbour
Pale Lantern
Gravelin
Wake Me Slow
Korvath

Here's a couple of the tracks that I put up, just to help you catch the vibe, if that helps.
https://tunebarrow.example/dariowelk/korvath-instrumental
https://tunebarrow.example/dariowelk/quiet-on-halden-instrumental
https://tunebarrow.example/dariowelk/rust-and-hollow-instrumental-1

Here's a few examples of some cover art that caught my eye. I don't want a carbon copy of these covers, but I absolutely love the atmosphere and the vibe that they create - smoky, etheral, trippy/glitchy yet weirdly beautiful, that kind of stuff generally. Just a general idea of the mood I'm looking for coverwise. I've also attached a couple photos of myself (one from the front, one from the side) so that if you decide you wanted to work a drawing of that into the front cover or the back cover you have that option if that's the vibe you're feeling. I'm trying to give you as much information as possible so that this process is easy, I hope the info I've given you is adequate. Overall I'm just looking for a cover/rear cover that will best accompany the music I've made, and I trust you will be able to help me achieve this.

Some examples of covers that I really like the atmosphere of (they're all pretty different so it might be worth taking a look at them):
Example 1: https://www.vidplume.example/watch?v=7tkaRMWepLoQ
Example 2: https://www.vidplume.example/watch?v=hQz-pwK8nbe&list=PL7rTMQ_2xbHc4gfkeWsLJAm3DqPodZt&index=105
Example 3: https://www.vidplume.example/watch?v=9-hDRtKxwmo&index=22&list=FLBz_tqW4_cuN3Rh8kdoaTVe
Example 4: https://www.vidplume.example/watch?v=eyT4LPQm7zk

If you need any more information, please contact me at dariowelk@mailrook.example and I'll be happy to give you any more information you'd like. Thank you very much.

Requirements
Must have
• Lo-fi, retro feel, doesn't look like a word-art collage. Preferably the album name/artist name in smallish writing (some jagged font) so that the main focus is whatever the main image on the cover is. Also I'd prefer it if there were just one image on the front cover, which takes up the whole cover, and then the artist name/album title on the front but not very large so that the main focus is whatever the image is. Again, lo-fi, dark, atmospheric, trippy is the way to go. Please no images of people. If you want to see some examples of covers that I liked check the project description because there are links in there to some covers that I liked.

```html
<!DOCTYPE html>
<html lang="en">
<head>
<meta charset="utf-8">
<title>Marrow Tide — Dario Welk — Back Cover</title>
<link rel="stylesheet" href="https://fonts.googleapis.com/css2?family=Josefin+Sans:ital,wght@1,300;1,400&display=swap">
<style>
  :root {
    --ink-black: #000000;
    --amber: #f6a52c;
    --amber-deep: #8a520f;
    --amber-dusk: #2a1703;
  }
  html, body {
    margin: 0;
    padding: 0;
    background: var(--ink-black);
    overflow: hidden;
  }
  .back-cover {
    position: relative;
    width: 1200px;
    height: 1200px;
    background: var(--ink-black);
    overflow: hidden;
  }
  .artwork-field {
    position: absolute;
    inset: 0;
    width: 1200px;
    height: 1200px;
  }
  .artwork-field .glow-start { stop-color: var(--amber); stop-opacity: 0.55; }
  .artwork-field .glow-mid { stop-color: var(--amber-deep); stop-opacity: 0.45; }
  .artwork-field .glow-end { stop-color: var(--amber-dusk); stop-opacity: 0.6; }
  .tracklist {
    position: absolute;
    left: 889px;
    top: 429px;
    margin: 0;
    padding: 0;
    list-style: none;
    transform: translateX(-50%);
    text-align: center;
    font-family: "Josefin Sans", "Century Gothic", sans-serif;
    font-style: italic;
    font-weight: 300;
    font-size: 37px;
    line-height: 89px;
    color: var(--amber);
    white-space: nowrap;
  }
</style>
</head>
<body>
  <main class="back-cover">
    <svg class="artwork-field" viewBox="0 0 1200 1200" role="img"
         aria-label="Artwork area: abstract amber wedge of light converging from the upper left toward the tracklist">
      <defs>
        <linearGradient id="wedge-glow" x1="1" y1="0" x2="0" y2="1">
          <stop offset="0" class="glow-start"/>
          <stop offset="0.5" class="glow-mid"/>
          <stop offset="1" class="glow-end"/>
        </linearGradient>
      </defs>
      <polygon points="0,0 1200,0 625,525 25,1200 0,1200" fill="url(#wedge-glow)"/>
    </svg>

    <ol class="tracklist">
      <li class="track">Quiet on Halden</li>
      <li class="track">Glass Ember</li>
      <li class="track">Rust and Hollow</li>
      <li class="track">Slow Hymn for the Harbour</li>
      <li class="track">Pale Lantern</li>
      <li class="track">Gravelin</li>
      <li class="track">Wake Me Slow</li>
      <li class="track">Korvath</li>
    </ol>
  </main>
</body>
</html>
```